Business Card Design

Personal training studio. My colors are burnt orange and grey. Specializing in group training and total body composition change. Nutritional consultant and contest prep.

Target Market(s)

My audience are people who are looking for total body composition change as well as knowledge on how to effectively receive results in the gym that they are a member of.

Industry/Entity Type

Training

Contact Information for Business Card

Dr. Maris Thackery
Marisjthackery@plumvane.com
3129071436
2815 west Brell ave.
Fennick Illinois 60794

Colors
f37122
aaaaaa

Requirements
Must have
• Animphasis on gaining knowledge that will sustain them for a life time. Healthy results and notice me results.
Nice to have
• Card should correlate with the colors of the studio. Orange and grey. With black flooring with orange speckles in it.

```html
<!DOCTYPE html>
<html lang="en">
<head>
<meta charset="utf-8">
<title>Thackery Form Studio – Business Card</title>
<link href="https://fonts.googleapis.com/css2?family=Open+Sans:wght@400;700&display=swap" rel="stylesheet">
<style>
  :root {
    --orange: #f37122;
    --orange-light: #f79a5c;
    --grey: #aaaaaa;
    --card: #0c0b0b;
    --backdrop: #3a3a3c;
    --white: #ffffff;
  }
  * { box-sizing: border-box; margin: 0; padding: 0; }
  html, body {
    width: 1200px; height: 780px; overflow: hidden;
    background: var(--backdrop);
    font-family: "Open Sans", Arial, sans-serif;
  }
  .sheet {
    width: 1200px; height: 780px;
    display: flex; align-items: center; justify-content: center; gap: 50px;
  }
  .card {
    position: relative;
    width: 525px; height: 300px;
    background: var(--card);
    overflow: hidden;
    box-shadow: 0 10px 28px rgba(0,0,0,.45);
  }

  /* brand lockup */
  .brand {
    position: absolute;
    display: flex; align-items: center; gap: 14px;
    white-space: nowrap;
  }
  .brand-dot {
    border-radius: 50%;
    background: var(--orange);
    flex: none;
  }
  .brand-name {
    color: var(--white);
    font-weight: 700;
    text-transform: uppercase;
    letter-spacing: .06em;
    line-height: 1.15;
  }

  .card-front .brand {
    left: 50%; top: 50%; transform: translate(-50%, -50%);
  }
  .card-front .brand-dot { width: 78px; height: 78px; }
  .card-front .brand-name { font-size: 26px; }

  .card-back .brand { right: 30px; top: 30px; gap: 10px; }
  .card-back .brand-dot { width: 44px; height: 44px; }
  .card-back .brand-name { font-size: 15px; }

  /* contact list */
  .contact {
    position: absolute; left: 30px; top: 30px;
    list-style: none;
    color: var(--orange);
    font-size: 13px;
    line-height: 1.25;
  }
  .contact li { display: flex; align-items: flex-start; gap: 8px; margin-bottom: 6px; }
  .contact svg { width: 13px; height: 13px; flex: none; margin-top: 2px; fill: var(--orange); }
  .contact .phone { font-size: 19px; font-weight: 700; }
  .contact .phone svg { margin-top: 5px; }

  .swoosh { position: absolute; left: 0; top: 0; width: 525px; height: 300px; }

  .holder {
    position: absolute; right: 34px; bottom: 34px;
    color: var(--orange);
    font-size: 22px; font-weight: 700;
    padding-bottom: 4px;
    border-bottom: 3px solid var(--orange);
    white-space: nowrap;
  }
</style>
</head>
<body>
<main class="sheet">

  <section class="card card-front" aria-label="Card front">
    <div class="brand">
      <span class="brand-dot"></span>
      <span class="brand-name">Thackery<br>Form Studio</span>
    </div>
  </section>

  <section class="card card-back" aria-label="Card back">
    <svg class="swoosh" viewBox="0 0 525 300" aria-hidden="true">
      <path d="M0 300 C90 200 260 150 525 160 L525 172 C280 170 110 215 20 300 Z" fill="var(--orange)"/>
      <path d="M150 205 C260 165 400 155 525 150 L525 155 C400 162 270 175 150 205 Z" fill="var(--orange)"/>
    </svg>

    <ul class="contact">
      <li class="phone">
        <svg viewBox="0 0 24 24"><path d="M6.6 10.8a15.1 15.1 0 0 0 6.6 6.6l2.2-2.2a1 1 0 0 1 1-.25 11.4 11.4 0 0 0 3.6.57 1 1 0 0 1 1 1V20a1 1 0 0 1-1 1A17 17 0 0 1 3 4a1 1 0 0 1 1-1h3.5a1 1 0 0 1 1 1c0 1.25.2 2.45.57 3.6a1 1 0 0 1-.25 1z"/></svg>
        <span>312 907 1436</span>
      </li>
      <li>
        <svg viewBox="0 0 24 24"><path d="M12 2a7 7 0 0 0-7 7c0 5.25 7 13 7 13s7-7.75 7-13a7 7 0 0 0-7-7zm0 9.5A2.5 2.5 0 1 1 12 6.5a2.5 2.5 0 0 1 0 5z"/></svg>
        <span>2815 west Brell ave.<br>Fennick Illinois 60794</span>
      </li>
      <li>
        <svg viewBox="0 0 24 24"><path d="M3 5h18a1 1 0 0 1 1 1v12a1 1 0 0 1-1 1H3a1 1 0 0 1-1-1V6a1 1 0 0 1 1-1zm9 7.5L4 7.4V9l8 5 8-5V7.4z"/></svg>
        <span>Marisjthackery@plumvane.com</span>
      </li>
    </ul>

    <div class="brand">
      <span class="brand-dot"></span>
      <span class="brand-name">Thackery<br>Form Studio</span>
    </div>

    <p class="holder">Dr. Maris Thackery</p>
  </section>

</main>
</body>
</html>
```